Build a Web page - Dorian Pellway Homes, LLC - a custom home builder

We are a custom home builder in Wisconsin. Need a basic web page with a home page, About Us, Contact info, Gallery, and Testimonials page. Gallery will probably have sub-pages and each will have about ten pictures or less. I already own the domain and have web hosting through Wix, I just need the site built. Once the page is built I should be able to do the upkeep on it myself. If I need to add pictures or whatever.
Updates

Project Deadline Extended
Reason: I am still looking through designs and will select soon - thank you!

Target Market(s)

Gen X and Millennials who are looking to build a home. Custom built homes - not generic spec homes.

Industry/Entity Type

Home Builder

Number of Pages Required

5+ page

Font styles to use
Sans Serif

Colors
ffffff
ec1f27
000000
9d9d9d

Requirements
Must have
• I have no idea if I want coded or in coded. I'm not sure of the difference and why I would want one over the other.
Nice to have
• We like the following colors - red, black, gray, white.
Should not have
• not a big fan of clip art like hammers, tape measures, etc. Must look professional.

```html
<!DOCTYPE html>
<html lang="en">
<head>
<meta charset="utf-8">
<title>Dorian Pellway Homes, LLC</title>
<link href="https://fonts.googleapis.com/css2?family=Open+Sans:wght@400;600;700;800&display=swap" rel="stylesheet">
<style>
:root{
  --red:#ec1f27;
  --black:#000000;
  --ink:#2b2b2b;
  --gray:#9d9d9d;
  --light:#f4f4f4;
  --white:#ffffff;
  --footer:#1b1b1b;
  --footer-deep:#111111;
}
*{box-sizing:border-box;margin:0;padding:0}
html,body{width:1200px;height:3805px;overflow:hidden}
body{font-family:"Open Sans",Arial,sans-serif;color:var(--ink);background:var(--white);position:relative}
a{color:inherit;text-decoration:none}

/* header */
.topbar{position:absolute;top:0;left:0;width:1200px;height:38px;background:var(--white);font-size:12px;color:#666}
.topbar .contact{position:absolute;right:38px;top:11px;display:flex;gap:34px}
.topbar .contact span{display:flex;align-items:center;gap:8px}
.navbar{position:absolute;top:38px;left:0;width:1200px;height:56px;background:rgba(255,255,255,.92);z-index:3}
.nav{position:absolute;right:38px;top:0;display:flex;height:56px;align-items:center}
.nav a{font-size:13px;font-weight:600;padding:0 19px;line-height:56px;color:#333;text-transform:uppercase}
.nav a.active{color:var(--red);border-bottom:3px solid var(--red);line-height:53px}
.brand{position:absolute;left:38px;top:38px;width:145px;height:140px;background:var(--white);z-index:4;box-shadow:0 2px 8px rgba(0,0,0,.15);display:flex;flex-direction:column;align-items:center;justify-content:center;gap:10px}
.brand .mark{width:16px;height:16px;background:var(--red)}
.brand .name{font-size:15px;font-weight:700;color:var(--ink);text-align:center;line-height:1.25;letter-spacing:.5px}

/* hero */
.hero{position:absolute;top:38px;left:0;width:1200px;height:647px;overflow:hidden}
.hero .photo{position:absolute;inset:0;background:linear-gradient(180deg,#7d9cc4 0%,#a9bfd8 25%,#6f7a5e 55%,#5e6b47 75%,#4f7a35 100%)}
.hero .shade{position:absolute;inset:0;background:rgba(0,0,0,.28)}
.hero .copy{position:absolute;left:0;right:0;top:277px;text-align:center;color:var(--white)}
.hero h1{font-size:33px;font-weight:800;letter-spacing:.5px;text-transform:uppercase}
.hero p{width:690px;margin:18px auto 0;font-size:14px;line-height:22px}
.btn{display:inline-flex;align-items:center;gap:8px;margin-top:20px;background:var(--red);color:var(--white);font-size:12px;font-weight:600;text-transform:uppercase;padding:10px 24px;border-radius:20px}
.hero .dots{position:absolute;left:0;right:0;top:606px;display:flex;justify-content:center;gap:8px}
.hero .dots i{width:13px;height:13px;border:2px solid var(--white);border-radius:50%}
.hero .dots i.on{border-color:var(--red);background:var(--red)}
.hero .curve{position:absolute;left:0;bottom:0;width:1200px;height:90px}

/* promo */
.promo{position:absolute;top:751px;left:38px;width:1124px;height:239px;display:grid;grid-template-columns:repeat(3,1fr);gap:3px}
.promo .tile{position:relative;overflow:hidden}
.promo .tile .photo{position:absolute;inset:0}
.promo .tile:nth-child(1) .photo{background:linear-gradient(135deg,#a8adab,#d4d2cb 60%,#8a7c6b)}
.promo .tile:nth-child(2) .photo{background:linear-gradient(135deg,#5e3b2b,#b89476 55%,#e3d3bf)}
.promo .tile:nth-child(3) .photo{background:linear-gradient(135deg,#c9c6c0,#e7e3dc 60%,#a39a8c)}
.promo .box{position:absolute;left:18px;right:18px;top:20px;bottom:20px;background:rgba(255,255,255,.85);display:flex;flex-direction:column;align-items:center;justify-content:center;text-align:center}
.promo .kicker{font-size:12px;font-weight:700;color:var(--ink);text-transform:uppercase}
.promo .title{font-size:26px;font-weight:700;color:var(--ink);text-transform:uppercase;line-height:1.2}
.promo .sub{font-size:12px;color:var(--gray)}

/* section headings */
.heading{position:absolute;left:0;width:1200px;text-align:center}
.heading h2{font-size:24px;font-weight:700;color:var(--ink);text-transform:uppercase;letter-spacing:1px}
.heading h2 em{font-style:normal;color:var(--red)}
.divider{display:block;margin:16px auto 0}

/* welcome */
.welcome-text{position:absolute;left:220px;width:760px;top:1140px;text-align:center;font-size:14px;line-height:29px;color:var(--gray)}
.welcome-text p+p{margin-top:29px}

/* gallery */
.gallery{position:absolute;top:1603px;left:38px;width:1124px;height:612px;display:grid;grid-template-columns:repeat(4,1fr);grid-template-rows:repeat(4,1fr);gap:3px}
.gallery .cell{position:relative}
.g1{grid-column:1/3;grid-row:1/3;background:linear-gradient(135deg,#b9a893,#f0e6d4 45%,#7a4c3a)}
.g2{background:linear-gradient(135deg,#8a6a55,#d3c5b3)}
.g3{background:linear-gradient(135deg,#6d5a48,#c8bca9)}
.g4{background:linear-gradient(180deg,#9fb7d3,#7a5a4a 60%,#6e8a4e)}
.g5{background:linear-gradient(180deg,#d8dde3,#8b5b3e 60%,#9aa08c)}
.g6{background:linear-gradient(135deg,#b7a66e,#e9e3cf)}
.g7{background:linear-gradient(180deg,#c9d2dc,#8c8a7a 60%,#6f7d4d)}
.g8{background:linear-gradient(135deg,#dad8d2,#6f6a62)}
.g9{background:linear-gradient(180deg,#9ab4cf,#7c8273 55%,#5d7a3c)}
.g10{grid-column:3;grid-row:3/5;background:linear-gradient(135deg,#6b4426,#b7865a 50%,#2f3c32)}
.g11{grid-column:4;grid-row:3/5;background:linear-gradient(135deg,#d8d4cc,#8a7f70 60%,#4c3a33)}
.g1 .overlay{position:absolute;inset:18px;border:2px solid rgba(255,255,255,.85)}
.g1 .label{position:absolute;left:30px;right:30px;top:110px;height:46px;background:rgba(0,0,0,.75);color:var(--white);font-size:18px;font-weight:600;text-transform:uppercase;display:flex;align-items:center;justify-content:center}

/* team */
.team-intro{position:absolute;top:2372px;left:100px;width:1000px;text-align:center;font-size:13px;line-height:21px;color:var(--gray)}
.team{position:absolute;top:2440px;left:53px;width:1091px;display:grid;grid-template-columns:repeat(4,252px);gap:27px}
.member{text-align:center}
.member .portrait{position:relative;height:287px;border:1px solid #ddd}
.member .portrait .photo{position:absolute;inset:0;background:linear-gradient(180deg,#fafafa,#e9e9e9)}
.member.focus .portrait .photo{background:#444}
.social{position:absolute;left:0;right:0;bottom:-14px;display:flex;justify-content:center;gap:6px}
.member.focus .social{bottom:auto;top:130px}
.social i{width:27px;height:27px;border-radius:50%;background:var(--red)}
.member h3{margin-top:32px;font-size:15px;font-weight:700;text-transform:uppercase;color:var(--ink)}
.member .role{font-size:12px;color:#777;margin-top:4px}
.member p{font-size:12px;line-height:18px;color:#888;margin-top:8px;padding:0 18px}
.arrow{position:absolute;top:2575px;width:28px;height:28px;border:1px solid #ddd;background:var(--white);display:flex;align-items:center;justify-content:center}

/* testimonials */
.testimonial{position:absolute;top:3062px;left:0;width:1200px;height:388px;overflow:hidden}
.testimonial .photo{position:absolute;inset:0;background:linear-gradient(90deg,#4a3a2e,#8a7867 40%,#6b5c4e 70%,#3a2f27)}
.testimonial .shade{position:absolute;inset:0;background:rgba(0,0,0,.55)}
.testimonial .quote{position:absolute;left:0;right:0;top:40px;text-align:center;color:var(--white);font-size:48px;font-weight:700;line-height:1}
.testimonial blockquote{position:absolute;left:115px;width:970px;top:118px;text-align:center;color:var(--white);font-size:15px;line-height:26px}
.testimonial cite{position:absolute;left:0;right:0;top:258px;text-align:center;color:var(--red);font-style:normal;font-size:14px;font-weight:600}
.testimonial .bars{position:absolute;left:0;right:0;top:334px;display:flex;justify-content:center;gap:10px}
.testimonial .bars i{width:38px;height:5px;background:var(--white)}
.testimonial .bars i.on{background:var(--red)}

/* footer */
.footer{position:absolute;top:3455px;left:0;width:1200px;height:300px;background:var(--footer);color:#ccc;font-size:13px}
.footer h4{font-size:16px;font-weight:700;color:var(--white);margin-bottom:24px}
.footer .col{position:absolute;top:78px}
.menu{display:grid;grid-template-columns:170px 170px;row-gap:10px}
.menu a{display:flex;align-items:center;gap:8px}
.contact-list li{list-style:none;display:flex;gap:14px;margin-bottom:14px;line-height:19px}
.hours{display:grid;grid-template-columns:120px 100px;row-gap:8px}
.footer .squares{display:flex;gap:10px;margin-top:26px}
.footer .squares i{width:36px;height:36px;border:1px solid #777}
.copyright{position:absolute;top:3755px;left:0;width:1200px;height:50px;background:var(--footer-deep);color:#aaa;font-size:12px;display:flex;align-items:center;justify-content:center}
.copyright em{font-style:normal;color:var(--red);margin:0 4px}
</style>
</head>
<body>

<div class="topbar">
  <div class="contact">
    <span><svg width="12" height="12" viewBox="0 0 24 24"><path d="M6.6 10.8a15 15 0 0 0 6.6 6.6l2.2-2.2a1 1 0 0 1 1-.25 11.4 11.4 0 0 0 3.6.6 1 1 0 0 1 1 1V20a1 1 0 0 1-1 1A17 17 0 0 1 3 4a1 1 0 0 1 1-1h3.5a1 1 0 0 1 1 1 11.4 11.4 0 0 0 .6 3.6 1 1 0 0 1-.25 1z" fill="#777"/></svg>+123 555 0142</span>
    <span><svg width="13" height="11" viewBox="0 0 24 18"><rect x="1" y="1" width="22" height="16" fill="none" stroke="#777" stroke-width="2"/><path d="M1 1l11 9 11-9" fill="none" stroke="#777" stroke-width="2"/></svg>info@dorianpellwayhomes.com</span>
  </div>
</div>

<section class="hero">
  <div class="photo" role="img" aria-label="Photo of a green two-storey family home on a lawn under a cloudy sky"></div>
  <div class="shade"></div>
  <div class="copy">
    <h1>Lorem ipsum dolor sit amet...</h1>
    <p>Lorem Ipsum is simply dummy text of the printing and typesetting industry. Lorem Ipsum has been the industry's standard dummy text ever since the 1500s, when an unknown printer took a galley of type and scrambled it to make a type specimen book.</p>
    <a class="btn" href="#">Read more <svg width="12" height="10" viewBox="0 0 12 10"><path d="M0 5h10M6 1l4 4-4 4" stroke="#fff" stroke-width="1.6" fill="none"/></svg></a>
  </div>
  <div class="dots"><i></i><i class="on"></i><i></i></div>
  <svg class="curve" viewBox="0 0 1200 90" preserveAspectRatio="none"><path d="M0 0 Q600 120 1200 0 L1200 90 L0 90 Z" fill="#ffffff"/></svg>
</section>

<div class="navbar">
  <nav class="nav">
    <a class="active" href="#">Home</a>
    <a href="#">About us</a>
    <a href="#">Gallery</a>
    <a href="#">Testimonials</a>
    <a href="#">Contact us</a>
  </nav>
</div>

<a class="brand" href="#"><span class="mark"></span><span class="name">DORIAN<br>PELLWAY<br>HOMES</span></a>

<section class="promo">
  <div class="tile"><div class="photo" role="img" aria-label="Photo of a bright living room interior"></div><div class="box"><span class="kicker">Get the new look</span><span class="title">New design</span><span class="sub">Furniture Collection</span></div></div>
  <div class="tile"><div class="photo" role="img" aria-label="Photo of a wooden deck and doorway"></div><div class="box"><span class="kicker">Get the new look</span><span class="title">New home design</span><span class="sub">Furniture Collection</span></div></div>
  <div class="tile"><div class="photo" role="img" aria-label="Photo of a modern white kitchen"></div><div class="box"><span class="kicker">Get the new look</span><span class="title">New design</span><span class="sub">Furniture Collection</span></div></div>
</section>

<div class="heading" style="top:1048px">
  <h2>Welcome to <em>Dorian Pellway Homes</em></h2>
  <svg class="divider" width="230" height="16" viewBox="0 0 230 16"><line x1="0" y1="8" x2="98" y2="8" stroke="#ccc"/><line x1="132" y1="8" x2="230" y2="8" stroke="#ccc"/><rect x="108" y="1" width="14" height="14" transform="rotate(45 115 8)" fill="none" stroke="#ec1f27" stroke-width="1.5"/><rect x="111.5" y="4.5" width="7" height="7" transform="rotate(45 115 8)" fill="#ec1f27"/></svg>
</div>
<div class="welcome-text">
  <p>Lorem Ipsum is simply dummy text of the printing and typesetting industry. Lorem Ipsum has been the industry's standard dummy text ever since the 1500s, when an unknown printer took a galley of type and scrambled it to make a type specimen book. It has survived not only five centuries, but also the leap into electronic typesetting, remaining essentially unchanged.</p>
  <p>It was popularised in the 1960s with the release of Tessaline sheets containing Lorem Ipsum passages, and more recently with desktop publishing software like Vellum Pagecraft including versions of Lorem Ipsum.</p>
  <p>Ut enim ad minim veniam, quis nostrud exercitation ullamco laboris nisi ut aliquip ex ea commodo consequat. Duis aute irure dolor in reprehenderit in voluptate velit esse cillum dolore eu fugiat nulla pariatur.</p>
</div>

<div class="heading" style="top:1500px">
  <h2>Our <em>Gallery</em></h2>
  <svg class="divider" width="230" height="16" viewBox="0 0 230 16"><line x1="0" y1="8" x2="98" y2="8" stroke="#ccc"/><line x1="132" y1="8" x2="230" y2="8" stroke="#ccc"/><rect x="108" y="1" width="14" height="14" transform="rotate(45 115 8)" fill="none" stroke="#ec1f27" stroke-width="1.5"/><rect x="111.5" y="4.5" width="7" height="7" transform="rotate(45 115 8)" fill="#ec1f27"/></svg>
</div>
<section class="gallery">
  <div class="cell g1" role="img" aria-label="Photo of a living room with sofas and a fireplace"><div class="overlay"></div><div class="label">New home design</div></div>
  <div class="cell g2" role="img" aria-label="Photo of a family room with a sectional sofa"></div>
  <div class="cell g3" role="img" aria-label="Photo of a living room with fireplace and television"></div>
  <div class="cell g4" role="img" aria-label="Photo of a red two-storey house exterior"></div>
  <div class="cell g5" role="img" aria-label="Photo of a wooden back deck"></div>
  <div class="cell g6" role="img" aria-label="Photo of a bathroom vanity"></div>
  <div class="cell g7" role="img" aria-label="Photo of a single-storey house with garage"></div>
  <div class="cell g8" role="img" aria-label="Photo of a laundry room"></div>
  <div class="cell g9" role="img" aria-label="Photo of a ranch house on a green lawn"></div>
  <div class="cell g10" role="img" aria-label="Photo of a kitchen with wooden cabinets"></div>
  <div class="cell g11" role="img" aria-label="Photo of an open dining room and kitchen"></div>
</section>

<div class="heading" style="top:2276px">
  <h2>Our <em>Team</em></h2>
  <svg class="divider" width="230" height="16" viewBox="0 0 230 16"><line x1="0" y1="8" x2="98" y2="8" stroke="#ccc"/><line x1="132" y1="8" x2="230" y2="8" stroke="#ccc"/><rect x="108" y="1" width="14" height="14" transform="rotate(45 115 8)" fill="none" stroke="#ec1f27" stroke-width="1.5"/><rect x="111.5" y="4.5" width="7" height="7" transform="rotate(45 115 8)" fill="#ec1f27"/></svg>
</div>
<p class="team-intro">Lorem Ipsum is simply dummy text of the printing and typesetting industry. Lorem Ipsum has been the industry's standard dummy text ever since the 1500s, when an unknown printer took a galley of type and scrambled it to make a type specimen book.</p>

<a class="arrow" href="#" style="left:38px"><svg width="14" height="10" viewBox="0 0 14 10"><path d="M14 5H2M6 1L2 5l4 4" stroke="#ec1f27" stroke-width="1.6" fill="none"/></svg></a>
<a class="arrow" href="#" style="left:1134px"><svg width="14" height="10" viewBox="0 0 14 10"><path d="M0 5h12M8 1l4 4-4 4" stroke="#ec1f27" stroke-width="1.6" fill="none"/></svg></a>

<section class="team">
  <article class="member">
    <div class="portrait"><div class="photo" role="img" aria-label="Portrait of a team member in a dark suit"></div><div class="social"><i></i><i></i><i></i><i></i><i></i></div></div>
    <h3>Lorem ipsum</h3><div class="role">— CEO —</div>
    <p>Lorem ipsum dolor sit amet, consectetur adipiscing elit, sed do eiusmod tempor incididunt.</p>
  </article>
  <article class="member focus">
    <div class="portrait"><div class="photo" role="img" aria-label="Portrait of a team member in a dark suit"></div><div class="social"><i></i><i></i><i></i><i></i><i></i></div></div>
    <h3>Lorem ipsum</h3><div class="role">— CEO —</div>
    <p>Lorem ipsum dolor sit amet, consectetur adipiscing elit, sed do eiusmod tempor incididunt.</p>
  </article>
  <article class="member">
    <div class="portrait"><div class="photo" role="img" aria-label="Portrait of a team member in a light suit"></div><div class="social"><i></i><i></i><i></i><i></i><i></i></div></div>
    <h3>Lorem ipsum</h3><div class="role">— CEO —</div>
    <p>Lorem ipsum dolor sit amet, consectetur adipiscing elit, sed do eiusmod tempor incididunt.</p>
  </article>
  <article class="member">
    <div class="portrait"><div class="photo" role="img" aria-label="Portrait of a team member in a beige suit"></div><div class="social"><i></i><i></i><i></i><i></i><i></i></div></div>
    <h3>Lorem ipsum</h3><div class="role">— CEO —</div>
    <p>Lorem ipsum dolor sit amet, consectetur adipiscing elit, sed do eiusmod tempor incididunt.</p>
  </article>
</section>

<div class="heading" style="top:2958px">
  <h2>Testimonials</h2>
  <svg class="divider" width="230" height="16" viewBox="0 0 230 16"><line x1="0" y1="8" x2="98" y2="8" stroke="#ccc"/><line x1="132" y1="8" x2="230" y2="8" stroke="#ccc"/><rect x="108" y="1" width="14" height="14" transform="rotate(45 115 8)" fill="none" stroke="#ec1f27" stroke-width="1.5"/><rect x="111.5" y="4.5" width="7" height="7" transform="rotate(45 115 8)" fill="#ec1f27"/></svg>
</div>
<section class="testimonial">
  <div class="photo" role="img" aria-label="Photo of a cosy living room with a stone fireplace and bookshelves"></div>
  <div class="shade"></div>
  <div class="quote">“</div>
  <blockquote>Lorem ipsum dolor sit amet, consectetur adipiscing elit, sed do eiusmod tempor incididunt ut labore et dolore magna aliqua. Ut enim ad minim veniam, quis nostrud exercitation ullamco laboris nisi ut aliquip ex ea commodo consequat. Duis aute irure dolor in reprehenderit in voluptate velit esse cillum dolore eu fugiat nulla pariatur. Excepteur sint occaecat cupidatat non proident, sunt in culpa qui officia deserunt mollit anim id est laborum.</blockquote>
  <cite>Owen Hartley</cite>
  <div class="bars"><i></i><i class="on"></i><i></i></div>
</section>

<footer class="footer">
  <div class="col" style="left:38px">
    <h4>Menu Link</h4>
    <div class="menu">
      <a href="#"><svg width="12" height="8" viewBox="0 0 12 8"><path d="M0 4h10M7 1l3 3-3 3" stroke="#fff" stroke-width="1.4" fill="none"/></svg>Home</a>
      <a href="#"><svg width="12" height="8" viewBox="0 0 12 8"><path d="M0 4h10M7 1l3 3-3 3" stroke="#fff" stroke-width="1.4" fill="none"/></svg>About Us</a>
      <a href="#"><svg width="12" height="8" viewBox="0 0 12 8"><path d="M0 4h10M7 1l3 3-3 3" stroke="#fff" stroke-width="1.4" fill="none"/></svg>Gallery</a>
      <a href="#"><svg width="12" height="8" viewBox="0 0 12 8"><path d="M0 4h10M7 1l3 3-3 3" stroke="#fff" stroke-width="1.4" fill="none"/></svg>Testimonials</a>
      <a href="#"><svg width="12" height="8" viewBox="0 0 12 8"><path d="M0 4h10M7 1l3 3-3 3" stroke="#fff" stroke-width="1.4" fill="none"/></svg>Contact Us</a>
      <a href="#"><svg width="12" height="8" viewBox="0 0 12 8"><path d="M0 4h10M7 1l3 3-3 3" stroke="#fff" stroke-width="1.4" fill="none"/></svg>Term and condition</a>
      <a href="#"><svg width="12" height="8" viewBox="0 0 12 8"><path d="M0 4h10M7 1l3 3-3 3" stroke="#fff" stroke-width="1.4" fill="none"/></svg>Privacy Policy</a>
    </div>
  </div>
  <div class="col" style="left:525px">
    <h4>Contact Information</h4>
    <ul class="contact-list">
      <li><svg width="12" height="16" viewBox="0 0 12 16"><path d="M6 0a6 6 0 0 0-6 6c0 4.5 6 10 6 10s6-5.5 6-10a6 6 0 0 0-6-6zm0 8.5A2.5 2.5 0 1 1 6 3.5a2.5 2.5 0 0 1 0 5z" fill="#ccc"/></svg><span>15, Harbor Lane st.<br>12345, Lakeview, Lipsum.</span></li>
      <li><svg width="14" height="14" viewBox="0 0 24 24"><path d="M6.6 10.8a15 15 0 0 0 6.6 6.6l2.2-2.2a1 1 0 0 1 1-.25 11.4 11.4 0 0 0 3.6.6 1 1 0 0 1 1 1V20a1 1 0 0 1-1 1A17 17 0 0 1 3 4a1 1 0 0 1 1-1h3.5a1 1 0 0 1 1 1 11.4 11.4 0 0 0 .6 3.6 1 1 0 0 1-.25 1z" fill="#ccc"/></svg><span>+123 555 0142</span></li>
      <li><svg width="14" height="14" viewBox="0 0 24 24"><rect x="3" y="8" width="18" height="13" fill="none" stroke="#ccc" stroke-width="2"/><rect x="7" y="3" width="10" height="5" fill="none" stroke="#ccc" stroke-width="2"/></svg><span>+123 555 0143</span></li>
      <li><svg width="14" height="12" viewBox="0 0 24 18"><rect x="1" y="1" width="22" height="16" fill="none" stroke="#ccc" stroke-width="2"/><path d="M1 1l11 9 11-9" fill="none" stroke="#ccc" stroke-width="2"/></svg><span>info@dorianpellwayhomes.com</span></li>
    </ul>
  </div>
  <div class="col" style="left:873px">
    <h4>Opening Hours</h4>
    <div class="hours"><span>Mon to Sat</span><span>09:00 to 09:00</span><span>Sunday</span><span>Closed</span></div>
    <div class="squares"><i></i><i></i><i></i><i></i></div>
  </div>
</footer>
<div class="copyright">Copyright © 2017 <em>dorianpellwayhomes.com</em>. All Rights Reserved.</div>

</body>
</html>
```